Harriet Voss Consortium - Paediatric Lower Limb Surgery Agenda Forming Collective

A 2-sided A4 leaflet to explain the research priorities in Children's Orthopaedic Surgery.
We would like this to be similar to that produced previously by the physiotherapists.

```html
<!DOCTYPE html>
<html lang="en">
<head>
<meta charset="utf-8">
<title>Harriet Voss Consortium – Research Priorities Leaflet</title>
<link href="https://fonts.googleapis.com/css2?family=Arimo:ital,wght@0,400;0,700;1,700&family=Ubuntu:wght@300;700&family=Roboto+Condensed:wght@400;700&display=swap" rel="stylesheet">
<style>
:root{
  --backdrop:#d4d4d6;
  --paper:#f2f2f2;
  --navy-a:#4d4c9e;
  --navy-b:#2b2858;
  --magenta:#c0509a;
  --pink-soft:#eeaad8;
  --teal-a:#1d9fa8;
  --teal-b:#3fc6cc;
  --orange-a:#ec8a22;
  --orange-b:#fbc530;
  --number-gold:#f7b733;
  --number-pink:#f5cbe8;
  --number-navy:#3a387f;
  --white:#ffffff;
}
*{box-sizing:border-box;margin:0;padding:0}
html,body{width:1200px;height:862px;overflow:hidden}
body{background:var(--backdrop);position:relative;font-family:"Arimo",Arial,sans-serif}
.page{position:absolute;top:66px;width:505px;height:714px;background:var(--paper);overflow:hidden}
.page--front{left:76px}
.page--back{left:631px}
.layer{position:absolute;left:0;top:0}

/* front */
.partners{position:absolute;left:30px;top:16px;color:var(--white);font-weight:700;font-size:10px;line-height:1.25}
.partner{display:flex;align-items:center;gap:6px;margin-bottom:8px}
.partner__dot{width:8px;height:8px;border-radius:50%;background:var(--white);flex:none}
.masthead{position:absolute;left:31px;top:96px;width:460px}
.masthead__org{font-weight:400;font-size:31px;color:var(--pink-soft);line-height:1.1}
.masthead__title{font-weight:400;font-size:27px;color:var(--white);line-height:1.1;margin-top:4px}
.intro{position:absolute;left:27px;top:247px;width:452px;color:var(--magenta);font-size:15px;line-height:17.8px;text-align:justify}
.intro p+p{margin-top:18px}
.stage{position:absolute;color:var(--white);font-family:"Roboto Condensed",Arial,sans-serif;font-weight:400;font-size:14px;line-height:14.4px}
.stage__head{font-family:"Ubuntu",sans-serif;font-weight:700;font-size:20px;line-height:24px;margin-bottom:4px}
.stage--ask{left:31px;top:477px;width:138px}
.stage--analyse{left:184px;top:477px;width:142px;text-align:center}
.stage--prioritise{left:352px;top:477px;width:134px;text-align:right}

/* back */
.priorities__title{position:absolute;top:22px;width:100%;text-align:center;font-family:"Roboto Condensed",sans-serif;font-weight:700;font-size:22px;color:var(--magenta)}
.priority{position:absolute;color:var(--white);font-size:10.2px;line-height:12.3px;transform:translateY(-50%)}
.priority--left{left:60px;width:385px}
.priority--right{left:27px;width:390px}
.rank{position:absolute;font-family:"Ubuntu",sans-serif;font-weight:300;font-size:46px;line-height:1;transform:translate(-50%,-50%)}
.rank--gold{color:var(--number-gold)}
.rank--pink{color:var(--number-pink)}
.rank--navy{color:var(--number-navy)}
.thanks{position:absolute;left:27px;top:643px;width:478px}
.thanks__lead{font-style:italic;font-weight:700;font-size:9.4px;color:var(--navy-a)}
.thanks__label{font-size:8.6px;color:var(--magenta);margin-top:8px}
.thanks__list{list-style:none;display:grid;grid-template-columns:222px 1fr;font-size:8px;letter-spacing:-.2px;color:var(--magenta);line-height:11px;margin-top:4px;white-space:nowrap}
.thanks__list li::before{content:"• "}
</style>
</head>
<body>

<section class="page page--front">
  <svg class="layer" width="505" height="714" viewBox="0 0 505 714">
    <defs>
      <linearGradient id="mastGrad" x1="0" y1="0" x2="1" y2="1">
        <stop offset="0" stop-color="#4a3f93"/><stop offset="1" stop-color="#272250"/>
      </linearGradient>
      <linearGradient id="tealGrad" x1="0" y1="0" x2="1" y2="1">
        <stop offset="0" stop-color="var(--teal-a)"/><stop offset="1" stop-color="var(--teal-b)"/>
      </linearGradient>
      <linearGradient id="orangeGrad" x1="0" y1="0" x2="1" y2="1">
        <stop offset="0" stop-color="var(--orange-a)"/><stop offset="1" stop-color="var(--orange-b)"/>
      </linearGradient>
    </defs>
    <path d="M0,0 H505 V190 Q505,198 495,200 L252,200 L12,180 Q0,178 0,168 Z" fill="url(#mastGrad)"/>
    <path d="M0,438 L150,452 Q166,454 166,470 L166,658 Q166,672 152,674 L0,693 Z" fill="url(#tealGrad)"/>
    <rect x="174" y="464" width="161" height="206" rx="18" fill="var(--magenta)"/>
    <path d="M357,463 L505,438 L505,693 L357,672 Q343,670 343,656 L343,480 Q343,465 357,463 Z" fill="url(#orangeGrad)"/>
  </svg>

  <div class="partners">
    <div class="partner"><span class="partner__dot"></span>Northfield Orthopaedic Guild</div>
    <div class="partner">Kestrel Society for Children's Limb Surgery</div>
    <div class="partner">Marrowgate University</div>
  </div>

  <header class="masthead">
    <h1 class="masthead__org">Harriet Voss Consortium</h1>
    <h2 class="masthead__title">Paediatric Lower Limb Surgery Agenda Forming Collective</h2>
  </header>

  <div class="intro">
    <p>Surgery is often carried out amongst children with conditions that affect their legs, but in many conditions, it is not known which treatment works best. We need high-quality research to test which treatments are better for children.</p>
    <p>We reached out to everybody involved with children who have orthopaedic problems affecting their legs (from hip to toes), including children, parents, carers, charity workers, and all the professional groups. We asked all for their views on identifying the most important unanswered questions.</p>
  </div>

  <div class="stage stage--ask">
    <h3 class="stage__head">Stage 1</h3>
    <p>ASK – Our UK-wide survey of patients, carers, physiotherapists, nurses and surgeons asked “What is the most important unanswered question amongst children undergoing planned surgery for conditions affecting their legs”</p>
  </div>
  <div class="stage stage--analyse">
    <h3 class="stage__head">Stage 2</h3>
    <p>ANALYSE – We reviewed 1023 questions from 388 people, and sorted these into 76 unique themed questions.</p>
  </div>
  <div class="stage stage--prioritise">
    <h3 class="stage__head">Stage 3</h3>
    <p>PRIORITISE – From those we asked patients, carers, physiotherapists, nurses and surgeons to tell us “What are your top-10 most important questions”. This created a shortlist that were prioritized at a final workshop.</p>
  </div>
</section>

<section class="page page--back">
  <svg class="layer" width="505" height="714" viewBox="0 0 505 714">
    <defs>
      <linearGradient id="navyGrad" x1="0" y1="0" x2="1" y2="0">
        <stop offset="0" stop-color="var(--navy-a)"/><stop offset="1" stop-color="var(--navy-b)"/>
      </linearGradient>
      <linearGradient id="magGrad" x1="0" y1="0" x2="1" y2="0">
        <stop offset="0" stop-color="#c65aa1"/><stop offset="1" stop-color="#b94895"/>
      </linearGradient>
      <linearGradient id="tealBand" x1="0" y1="0" x2="1" y2="0">
        <stop offset="0" stop-color="var(--teal-a)"/><stop offset="1" stop-color="var(--teal-b)"/>
      </linearGradient>
      <linearGradient id="orangeBand" x1="0" y1="0" x2="1" y2="0">
        <stop offset="0" stop-color="var(--orange-a)"/><stop offset="1" stop-color="var(--orange-b)"/>
      </linearGradient>
    </defs>
    <path d="M0,66 Q0,57 10,57 L490,57 Q505,57 505,72 L505,78 Q505,88 492,89 L10,127 Q0,127 0,118 Z" fill="url(#navyGrad)"/>
    <path d="M0,140 Q0,131 10,131 L490,104 Q505,103 505,118 L505,172 Q505,182 492,182 L10,170 Q0,169 0,160 Z" fill="url(#magGrad)"/>
    <path d="M0,188 Q0,178 10,178 L495,184 Q430,226 320,232 L10,236 Q0,236 0,226 Z" fill="url(#tealBand)"/>
    <path d="M0,248 Q0,239 10,239 L490,212 Q505,211 505,226 L505,279 Q505,289 492,289 L10,274 Q0,273 0,264 Z" fill="url(#orangeBand)"/>
    <path d="M0,296 Q0,286 10,286 L490,286 Q505,286 505,300 L505,312 Q505,323 492,324 L10,356 Q0,356 0,347 Z" fill="url(#navyGrad)"/>
    <path d="M0,369 Q0,360 10,360 L490,331 Q505,330 505,345 L505,399 Q505,409 492,409 L10,393 Q0,392 0,383 Z" fill="url(#magGrad)"/>
    <path d="M0,416 Q0,406 10,406 L495,412 Q440,455 360,462 L10,466 Q0,466 0,456 Z" fill="url(#tealBand)"/>
    <path d="M0,476 Q0,467 10,467 L490,440 Q505,439 505,454 L505,507 Q505,517 492,517 L10,501 Q0,500 0,491 Z" fill="url(#orangeBand)"/>
    <path d="M0,523 Q0,513 10,513 L490,513 Q505,513 505,527 L505,541 Q505,552 492,553 L10,583 Q0,583 0,574 Z" fill="url(#navyGrad)"/>
    <path d="M0,596 Q0,587 10,587 L490,555 Q505,554 505,569 L505,611 Q505,621 492,621 L10,612 Q0,612 0,603 Z" fill="url(#magGrad)"/>
  </svg>

  <h2 class="priorities__title">OUR TOP-10 RESEARCH PRIORITIES:</h2>

  <span class="rank rank--gold" style="left:39px;top:88px">1</span>
  <p class="priority priority--left" style="top:88px">What are the best ways to measure the outcome following lower limb orthopaedic surgery in children?</p>

  <span class="rank rank--pink" style="left:468px;top:154px">2</span>
  <p class="priority priority--right" style="top:148px">Following orthopaedic surgery to the lower limbs, what should children's rehabilitation include, how long is it expected to last and how does it affect the result of treatment?</p>

  <span class="rank rank--gold" style="left:39px;top:208px">3</span>
  <p class="priority priority--left" style="top:207px">What is the short-term and long-term clinical and cost effectiveness of orthopaedic<br>lower limb surgery (including best timing and technique) for children<br>with Cerebral Palsy who can walk?</p>

  <span class="rank rank--navy" style="left:468px;top:249px">4</span>
  <p class="priority priority--right" style="top:253px">What are the short term and long term outcomes of surgery compared to non-surgical care in the treatment of Perthes disease of the hip?</p>

  <span class="rank rank--gold" style="left:39px;top:322px">5</span>
  <p class="priority priority--left" style="top:316px">What is the clinical and cost effectiveness of pre-operative rehabilitation in children presenting with lower limb orthopaedic conditions?</p>

  <span class="rank rank--pink" style="left:468px;top:372px">6</span>
  <p class="priority priority--right" style="top:375px">What is the short-term and long-term clinical and cost effectiveness of Selective Dorsal Rhizotomy (SDR) in children with Cerebral Palsy who can walk?</p>

  <span class="rank rank--gold" style="left:39px;top:436px">7</span>
  <p class="priority priority--left" style="top:438px">Can surveillance and non-surgical treatment (e.g. physiotherapy, botulinum<br>toxin injections, functional electrical stimulation, orthotics, casting) prevent the<br>development of deformity requiring surgery in children with Cerebral Palsy?</p>

  <span class="rank rank--navy" style="left:468px;top:484px">8</span>
  <p class="priority priority--right" style="top:490px">What is the best method of screening for Developmental Dysplasia of the Hip (DDH) in terms of clinical and cost effectiveness?</p>

  <span class="rank rank--gold" style="left:39px;top:546px">9</span>
  <p class="priority priority--left" style="top:544px">What are the best strategies to optimise communication of information between patients/carers and clinicians in order to enable shared decision-making?</p>

  <span class="rank rank--pink" style="left:464px;top:588px">10</span>
  <p class="priority priority--right" style="top:596px">What is the best management for hip displacement in children with Cerebral Palsy?</p>

  <footer class="thanks">
    <p class="thanks__lead">Many thanks to all those people who helped us take this work off the ground and helped us finish it!</p>
    <p class="thanks__label">Special thanks to:</p>
    <ul class="thanks__list">
      <li>The Kestrel Society for Children's Limb Surgery</li>
      <li>Marrowgate University and the</li>
      <li>The Northfield Orthopaedic Guild</li>
      <li>Harriet Voss Consortium, who always look for fair play in research!</li>
    </ul>
  </footer>
</section>

</body>
</html>
```